Need posters that inspire entrepreneurs

I want to create beautiful, inspiring wall art. I'm looking for a designer to create an awesome sample (note this sample is not for real use). The winning design will form the foundation of our art "style" so there will be LOTS of ongoing work for the winning designer.

It's your challenge to create a style that is clean, inspiring and timeless, and possibly can be adapted to different colour palettes.

Looking for a perfect execution of words, image and design.

The attached example shows one idea. It should serve as an idea only.

Format of the images should be either rectangular or square. Exact size is preferably UK A4 (US letter) or max A3. Assume that a display would consist of a 4 x 4 image grid so size needs to allow for that in a small to medium size office.

The quotes I want in the 3 samples (each in an individual poster - not combined in 1 poster). Each quote should have it's own, the reason for three is to prove the design work on more than one quote. The quotes are:

1) Failure is the condiment that gives success its flavor.
– Wendell Ruskin

2) Whether you think you can or think you can’t, you’re right.
– Milo Dagwell

3) Ever tried. Ever failed. No matter. Try Again. Fail again. Fail better.
– Oswin Tarrant

Each design should include the image of the person and the quote + any design elements you consider relevant. You should find relevant images of the individuals being quoted. The final images will not be published or used commercially in any way.

Font styles to use
Serif
Sans Serif

Colors

Designer to choose colors to be used in the design.

Requirements
Must have
• Words and headshot image - 1 per poster design.
• Please consider in the design that there will not always be photographs of the person quoted and as such the design will need to hold, whether the source is a photo, sketch or something else.
Nice to have
• None, but note that the final image will be printed on a wall mounted board, printed to the edge but not on the edge. The board will have black or white edges so consider in the design.
Should not have
• None

```html
<!DOCTYPE html>
<html lang="en">
<head>
<meta charset="utf-8">
<title>Entrepreneur Quote Posters</title>
<link rel="stylesheet" href="https://fonts.googleapis.com/css2?family=Kalam&family=Kurale&family=Fondamento:ital@1&family=Herr+Von+Muellerhoff&display=swap">
<style>
  :root {
    --sheet: #ffffff;
    --ink-light: #ffffff;
    --accent-red: #e0262b;
    --poster-black: #0b0b0b;
    --photo-dark: #2a2a2a;
    --photo-mid: #6e6e6e;
    --photo-light: #a9a9a9;
    --shadow: rgba(0,0,0,0.35);
  }
  html, body {
    margin: 0;
    padding: 0;
    width: 850px;
    height: 1200px;
    overflow: hidden;
    background: var(--sheet);
  }
  .sheet {
    position: relative;
    width: 850px;
    height: 1200px;
  }
  .poster {
    position: absolute;
    width: 489px;
    height: 346px;
    overflow: hidden;
    background: var(--poster-black);
    box-shadow: 1px 2px 3px var(--shadow);
  }
  .poster--condiment { left: 43px; top: 49px; }
  .poster--mindset { left: 175px; top: 427px; }
  .poster--persist { left: 306px; top: 808px; }

  .portrait {
    position: absolute;
    top: 0;
    right: 0;
    height: 100%;
  }
  .poster--condiment .portrait {
    width: 62%;
    background: radial-gradient(ellipse at 58% 40%, var(--photo-light) 0%, var(--photo-mid) 28%, var(--photo-dark) 55%, var(--poster-black) 85%);
  }
  .poster--mindset { background: linear-gradient(90deg, #121212 0%, #2b2b2b 60%, #1a1a1a 100%); }
  .poster--mindset .portrait {
    width: 55%;
    background: radial-gradient(ellipse at 45% 35%, #bdbdbd 0%, #7a7a7a 25%, #333 55%, rgba(20,20,20,0) 85%);
  }
  .poster--persist { background: linear-gradient(90deg, #3a3a3a 0%, #5a5a5a 50%, #484848 100%); }
  .poster--persist .portrait {
    width: 58%;
    background: radial-gradient(ellipse at 55% 38%, #d2d2d2 0%, #8d8d8d 28%, #3a3a3a 60%, rgba(40,40,40,0) 90%);
  }

  .quote {
    position: absolute;
    margin: 0;
    color: var(--ink-light);
    white-space: nowrap;
  }
  .quote--condiment {
    left: 26px;
    top: 22px;
    font-family: 'Kalam', cursive;
    font-size: 32px;
    line-height: 52px;
  }
  .quote--mindset {
    left: 30px;
    top: 30px;
    font-family: 'Kurale', serif;
    font-size: 32px;
    line-height: 31px;
    letter-spacing: 1px;
  }
  .quote--persist {
    left: 40px;
    top: 44px;
    font-family: 'Fondamento', serif;
    font-style: italic;
    font-size: 38px;
    line-height: 43px;
  }
  .quote-mark {
    position: absolute;
    left: 28px;
    top: 160px;
    color: var(--ink-light);
    font-family: Georgia, serif;
    font-weight: bold;
    font-size: 84px;
    line-height: 1;
  }
  .author {
    position: absolute;
    color: var(--accent-red);
    white-space: nowrap;
  }
  .author--condiment {
    left: 26px;
    top: 298px;
    font-family: 'Kalam', cursive;
    font-size: 23px;
  }
  .author--mindset {
    left: 42px;
    top: 276px;
    font-family: 'Herr Von Muellerhoff', cursive;
    font-size: 44px;
  }
  .author--persist {
    left: 288px;
    top: 280px;
    font-family: 'Herr Von Muellerhoff', cursive;
    font-size: 44px;
  }
</style>
</head>
<body>
<main class="sheet">

  <section class="poster poster--condiment">
    <div class="portrait" role="img" aria-label="Black and white portrait of Wendell Ruskin resting his cheek on his hand"></div>
    <p class="quote quote--condiment">Failure is the condiment<br>that gives success<br>its flavor...</p>
    <span class="author author--condiment">Wendell Ruskin</span>
  </section>

  <section class="poster poster--mindset">
    <div class="portrait" role="img" aria-label="Black and white portrait of Milo Dagwell in profile, chin on hand"></div>
    <p class="quote quote--mindset">Whether you think<br>you can or<br>think you can’t,<br>you’re right...</p>
    <span class="quote-mark">“</span>
    <span class="author author--mindset">Milo Dagwell</span>
  </section>

  <section class="poster poster--persist">
    <div class="portrait" role="img" aria-label="Black and white portrait of Oswin Tarrant smiling, glasses pushed up on his forehead"></div>
    <p class="quote quote--persist">Ever tried<br>Ever failed<br>No matter<br>Try Again<br>Fail again<br>Fail better...</p>
    <span class="author author--persist">Oswin Tarrant</span>
  </section>

</main>
</body>
</html>
```